Brisa Lumen Systems Corp Business Cards

Business cards to match the logo.

Company is a start up water technology company that has developed a patented system using centrifugal force to separate waste from municipal waste water to produce crystal clear clean water. Product sell starting at 2 million to governments both in the US and international.

Business cards should have a professional look with the target generally engineers.

Target Market(s)

Engineers, Government officials and investors

Industry/Entity Type

Water Treatment

Contact Information for Business Card

Business cards design will be used for 6 to 8 people with job titles. Can use the quote "If there is magic in the planet, it is contained in water." but not required to use quote. Should follow theme of Logo

Font styles to use
Other font styles liked:
• match logo font

Requirements
Nice to have
• Colors to match Logo. Business cards to match style of flow of Logo.
• Emphasis on clean look not a busy look. Clean flowing water.
Should not have
• Pictures of industrial equipment or wastewater

```html
<!DOCTYPE html>
<html lang="en">
<head>
<meta charset="utf-8">
<title>Brisa Lumen Systems Corp Business Cards</title>
<link href="https://fonts.googleapis.com/css2?family=Roboto:wght@400;500&display=swap" rel="stylesheet">
<style>
  :root {
    --backdrop: #2a2a2a;
    --paper: #f3f3f3;
    --navy: #15557f;
    --sky: #29aae1;
    --ink: #444444;
    --rule: #6d6d6d;
    --white: #ffffff;
  }
  * { margin: 0; padding: 0; box-sizing: border-box; }
  html, body { width: 1200px; height: 960px; overflow: hidden; }
  body {
    background: var(--backdrop);
    font-family: "Roboto", Arial, sans-serif;
    position: relative;
  }
  .card { position: absolute; width: 600px; height: 342px; }
  .card-front { left: 314px; top: 113px; background: var(--paper); }
  .card-back { left: 311px; top: 472px; background: var(--sky); }

  .brand-name {
    position: absolute;
    right: 34px;
    top: 80px;
    font-size: 30px;
    font-weight: 400;
    letter-spacing: 1px;
    color: var(--navy);
    white-space: nowrap;
  }
  .person { position: absolute; left: 36px; top: 174px; }
  .person-name { font-size: 21px; font-weight: 500; color: var(--navy); line-height: 24px; }
  .person-title { font-size: 15px; font-weight: 500; color: var(--sky); line-height: 18px; }
  .divider {
    position: absolute; left: 38px; top: 225px; width: 529px;
    height: 1px; background: var(--rule);
  }
  .contact-list { position: absolute; left: 36px; top: 238px; list-style: none; }
  .contact-item {
    display: flex; align-items: center; height: 19px;
    font-size: 14px; color: var(--ink);
  }
  .contact-icon { width: 16px; height: 14px; margin-right: 7px; fill: var(--navy); }
  .address {
    position: absolute; right: 34px; top: 262px; text-align: right;
    font-size: 14px; line-height: 18px; color: var(--ink);
  }
  .edge-band { position: absolute; left: 0; bottom: 0; width: 600px; height: 12px; }

  .back-brand {
    position: absolute; left: 0; right: 0; top: 150px; text-align: center;
    font-size: 36px; font-weight: 400; letter-spacing: 1px; color: var(--white);
  }
  .motto {
    position: absolute; left: 0; right: 0; top: 291px; text-align: center;
    font-size: 14px; color: var(--white);
  }
</style>
</head>
<body>
  <section class="card card-front">
    <div class="brand-name">BRISA LUMEN SYSTEMS</div>
    <div class="person">
      <div class="person-name">ELIAS MARREN</div>
      <div class="person-title">CEO/FOUNDER</div>
    </div>
    <div class="divider"></div>
    <ul class="contact-list">
      <li class="contact-item">
        <svg class="contact-icon" viewBox="0 0 16 14"><path d="M3 1l3 0 1 3-2 1.5c1 2 2.5 3.5 4.5 4.5L11 8l3 1v3c-6 1-12-5-11-11z"/></svg>555 210 4187
      </li>
      <li class="contact-item">
        <svg class="contact-icon" viewBox="0 0 16 14"><path d="M5 0h6a1 1 0 0 1 1 1v12a1 1 0 0 1-1 1H5a1 1 0 0 1-1-1V1a1 1 0 0 1 1-1zm1 2v8h4V2z"/></svg>555 362 9045
      </li>
      <li class="contact-item">
        <svg class="contact-icon" viewBox="0 0 16 14"><path d="M4 0h8v4H4zM1 5h14v6h-3v3H4v-3H1zm4 4v4h6V9z"/></svg>555 718 2263
      </li>
      <li class="contact-item">
        <svg class="contact-icon" viewBox="0 0 16 14"><path d="M1 3h14v9H1zm1 1l6 4 6-4z"/></svg>elias@brisalumen.com
      </li>
    </ul>
    <div class="address">
      2140 Harbor Ridge Road<br>
      Kestrel Bay, Alaska 34581<br>
      www.brisalumen.com
    </div>
    <svg class="edge-band" viewBox="0 0 600 12" aria-hidden="true">
      <polygon points="0,0 353,0 349,12 0,12" fill="var(--navy)"/>
      <polygon points="356,0 600,0 600,12 352,12" fill="var(--sky)"/>
    </svg>
  </section>

  <section class="card card-back">
    <div class="back-brand">BRISA LUMEN SYSTEMS</div>
    <p class="motto">If there is magic in the planet, it is contained in water.</p>
  </section>
</body>
</html>
```